lantern quill flyer

lantern quill, analysing tapes in reverse and hypnotherapy services - logo and design similar to website - http://www.lanternquill.com - flyer should be half A4 size - workshop on one side, training class on the other

Industry/Entity Type

Hypnotherapy

Colors
0455a3
3176b5

```html
<!DOCTYPE html>
<html lang="en">
<head>
<meta charset="utf-8">
<title>Lanternquill – Workshop and Training</title>
<link rel="stylesheet" href="https://fonts.googleapis.com/css2?family=Tinos&display=swap">
<style>
  :root {
    --flyer-blue: #3176b5;
    --ink-white: #ffffff;
  }
  html, body {
    margin: 0;
    padding: 0;
    overflow: hidden;
  }
  .flyer {
    position: relative;
    width: 845px;
    height: 1200px;
    background: var(--flyer-blue);
    color: var(--ink-white);
    font-family: "Tinos", "Times New Roman", serif;
    overflow: hidden;
  }
  .flyer__text {
    position: absolute;
    margin: 0;
    line-height: 1;
    font-weight: 400;
    white-space: nowrap;
  }
  .brand-name {
    left: 0;
    width: 822px;
    top: 167px;
    font-size: 56px;
    text-align: center;
  }
  .contact-city {
    left: 311px;
    top: 394px;
    font-size: 35px;
  }
  .contact-phone {
    left: 311px;
    top: 469px;
    font-size: 35px;
  }
  .contact-web {
    left: 344px;
    top: 740px;
    font-size: 37px;
  }
  .offer-line {
    left: 212px;
    top: 938px;
    font-size: 35px;
  }
  .icon {
    position: absolute;
    display: block;
  }
  .icon--phone {
    left: 211px;
    top: 455px;
    width: 66px;
    height: 66px;
  }
  .icon--globe {
    left: 211px;
    top: 720px;
    width: 83px;
    height: 83px;
  }
</style>
</head>
<body>
  <main class="flyer">
    <h1 class="flyer__text brand-name">Lanternquill</h1>

    <p class="flyer__text contact-city">London</p>

    <svg class="icon icon--phone" viewBox="0 0 66 66" aria-hidden="true">
      <rect x="0" y="0" width="66" height="66" rx="10" fill="var(--ink-white)"/>
      <path d="M24 14 c-4 1 -7 4 -7 9 c1 12 11 26 22 31 c5 2 9 1 11 -3 l-6 -7 c-1 -1 -3 -1 -4 0 l-3 2 c-6 -4 -10 -11 -12 -18 l3 -2 c1 -1 1 -3 0 -4 z"
            fill="var(--flyer-blue)"/>
    </svg>
    <p class="flyer__text contact-phone">0203 5550 184</p>

    <svg class="icon icon--globe" viewBox="0 0 83 83" aria-hidden="true">
      <g fill="none" stroke="var(--ink-white)" stroke-width="4">
        <circle cx="41.5" cy="41.5" r="38"/>
        <ellipse cx="41.5" cy="41.5" rx="17" ry="38"/>
        <line x1="41.5" y1="3.5" x2="41.5" y2="79.5"/>
        <line x1="3.5" y1="41.5" x2="79.5" y2="41.5"/>
        <line x1="9" y1="22" x2="74" y2="22"/>
        <line x1="9" y1="61" x2="74" y2="61"/>
      </g>
    </svg>
    <p class="flyer__text contact-web">www.lanternquill.com</p>

    <p class="flyer__text offer-line">Workshop and Training</p>
  </main>
</body>
</html>
```